EAT DIRT! Packaging redesign for Moonhops Energy Bites

We are redesigning our packaging for Moonhops Energy Bites, a healthy snack for people who want to build a better world. This brand is about action, health, and authenticity
Right now we need mockups of 4 different packaging aesthetics to survey customers about. We will then pick a winner and create a final design.
The four aesthetics are:
1. Hipster-ish
2. Vaporwave/retro
3. Kid-friendly
4. Hippy Snacks
We were working with a graphic designer who unfortunately passed away. We're hoping you can pick up where he left off. He completed a mockup for the hipster aesthetic, and a concept sketch for kid friendly.
The brand archetype for moonhops is Jester/Outlaw. Moonhop enthusiasts question mainstream assumptions about the world. We want to create better systems of spiritual actualization, and have as much fun as possible doing it.
Important points for the packaging:
-Drink water, breathe air, eat dirt
-Dates, Papaya, coconut
-Simple whole food ingredients
-Soft & chewy
-Made by humans
These will be custom printed, so don't feel constrained to the brown kraft paper. it can be any color we imagine. It important to have the window on the pouch, though.
A good job on this project WILL lead to more design work for you.

```html
<!DOCTYPE html>
<html lang="en">
<head>
<meta charset="utf-8">
<title>Moonhops Energy Bites – Pouch Front</title>
<link rel="stylesheet" href="https://fonts.googleapis.com/css2?family=Arvo:wght@700&family=Josefin+Sans:wght@600;700&display=swap">
<style>
  :root {
    --backdrop: #ececec;
    --pouch-light: #e8894a;
    --pouch-mid: #d4662a;
    --pouch-dark: #b9501a;
    --charcoal: #333231;
    --ribbon: #2f2d2c;
    --white: #ffffff;
    --window-label: #a9a9a9;
    --pattern-tone: rgba(245, 190, 160, 0.35);
  }
  * { margin: 0; padding: 0; box-sizing: border-box; }
  html, body { width: 1200px; height: 1200px; overflow: hidden; }
  body {
    position: relative;
    background: var(--backdrop);
    font-family: "Josefin Sans", sans-serif;
  }
  .pouch {
    position: absolute;
    left: 283px; top: 68px;
    width: 637px; height: 1097px;
    background: linear-gradient(100deg, var(--pouch-light) 0%, var(--pouch-mid) 45%, var(--pouch-dark) 100%);
    overflow: hidden;
  }
  .trail-texture {
    position: absolute; inset: 0;
    background: radial-gradient(ellipse at 70% 40%, var(--pattern-tone), transparent 60%),
                radial-gradient(ellipse at 25% 85%, var(--pattern-tone), transparent 55%);
  }
  .zip-line {
    position: absolute; left: 30px; right: 30px; top: 105px;
    height: 2px; background: rgba(120, 50, 10, 0.35);
  }
  .brand-block {
    position: absolute; left: 175px; top: 0;
    width: 297px; height: 332px;
    background: var(--charcoal);
    overflow: hidden;
  }
  .hang-hole {
    position: absolute; left: 60px; top: 32px;
    width: 180px; height: 62px;
    background: var(--white); border-radius: 31px;
  }
  .brand-name {
    position: absolute; left: 0; right: 0; top: 118px;
    text-align: center; color: var(--white);
    font-family: "Josefin Sans", sans-serif; font-weight: 700;
    font-size: 74px; line-height: 104px; letter-spacing: 1px;
  }
  .activity-art {
    position: absolute; left: 122px; top: 332px;
    width: 440px; height: 108px;
    background: linear-gradient(180deg, rgba(47,45,44,0.15), rgba(47,45,44,0.55));
    border-radius: 6px;
  }
  .ground-line {
    position: absolute; left: 102px; top: 441px;
    width: 460px; height: 2px; background: var(--ribbon);
  }
  .ribbon { position: absolute; left: 47px; top: 457px; }
  .ribbon-text {
    position: absolute; left: 47px; top: 457px; width: 540px; height: 52px;
    display: flex; align-items: center; justify-content: center;
    color: var(--white); font-weight: 600; font-size: 31px; letter-spacing: 4px;
    padding-top: 4px;
  }
  .tagline, .flavours {
    position: absolute; left: 0; right: 0; text-align: center;
    font-family: "Arvo", serif; font-weight: 700; color: var(--white);
    text-shadow: 2px 2px 3px rgba(40, 20, 10, 0.85);
  }
  .tagline { top: 527px; font-size: 33px; line-height: 37px; padding-left: 50px; }
  .window {
    position: absolute; left: 46px; top: 619px;
    width: 530px; height: 300px; border-radius: 50%;
    background: var(--white);
    display: flex; align-items: center; justify-content: center;
    color: var(--window-label); font-weight: 600; font-size: 27px; letter-spacing: 1px;
    padding-top: 12px;
  }
  .flavours { top: 938px; font-size: 44px; line-height: 44px; padding-left: 30px; }
</style>
</head>
<body>
  <div class="pouch">
    <div class="trail-texture" role="img" aria-label="Faint pattern of footprints and tyre tracks across the pouch"></div>
    <div class="zip-line"></div>

    <div class="brand-block">
      <div class="hang-hole"></div>
      <div class="brand-name">MOON<br>HOPS</div>
    </div>

    <div class="activity-art" role="img" aria-label="Silhouettes of a pine tree, a mountain biker, a hiker and a runner"></div>
    <div class="ground-line"></div>

    <svg class="ribbon" width="540" height="52" viewBox="0 0 540 52" aria-hidden="true">
      <polygon points="0,52 28,26 0,0 540,0 512,26 540,52" fill="var(--ribbon)"/>
    </svg>
    <div class="ribbon-text">FOR ACTIVE PEOPLE</div>

    <p class="tagline">Drink water, breathe air<br>eat dirt</p>

    <div class="window">CLEAR AREA</div>

    <p class="flavours">Dates • Papaya<br>Coconut</p>
  </div>
</body>
</html>
```